Poem Handwritten by Veteran while in the jungle of Vietnam

My parents are celebrating their 50th wedding anniversary this year. I wanted to give them a very memorable gift. On my parents 2nd anniversary, my father was stationed in Vietnam. On that night he was in the jungle waiting till morning and wrote a poem to my mother using his pant leg as paper. I would like this poem to typographically designed to be framed and hung on the wall.

I have attached a picture of the poem below. It will need to be 11x14 when printed for framing. It would be great if there was background or artwork to make it more visually interesting, perhaps in a watercolor. My parents have a transitional style. I have attached some possible color schemes as well. Cool greens, blue, neutral grays, with hints of berries or highlights of yellow. These are just a guide, I would be open to your interpretations.

Thank you for your help. This will hopefully be a gift they will truly treasure as much as the poem itself.

Target Market(s)

My parents who are excited to be celebrating their 50th wedding anniversary. It should have a transitional, mature style.

Font styles to use
Serif
Script

Requirements
Must have
• The poem, typographically designed. There can be a mix of fonts, but legibility is critically important.
• Now that some designs have come through I wanted to give some more guidance of what I'm looking for. I want something that feels sophisticated and artistic.
Nice to have
• A background or art work, using the color schemes attached as a guide. I am really liking the designs that have a full color landscape artwork in the background. The fonts should be elegant and formal. I really like the romantic, muted colors. I had trouble finding similar projects online in the style I wanted until I cam across wedding invites. Those seem to be the most applicable. I've added pictures of some so you can get a sense of what I'm looking for. I am really liking the jungle foliage, starry skies or sunrises.
Should not have
• Cartoon caricatures, fonts that are too illegible when printed. I'm not liking anything whimsical. I don't like the very bright colors for this project.

```html
<!DOCTYPE html>
<html lang="en">
<head>
<meta charset="utf-8">
<title>Life's Journey — Anniversary Poem</title>
<link rel="stylesheet" href="https://fonts.googleapis.com/css2?family=Great+Vibes&family=Questrial&display=swap">
<style>
  :root {
    --page: #ffffff;
    --navy: #272d42;
    --olive: #5b6429;
    --gold: #d9a640;
    --orange: #d88432;
    --ink: #f1f1ec;
  }
  html, body {
    margin: 0;
    padding: 0;
    width: 1200px;
    height: 1200px;
    overflow: hidden;
    background: var(--page);
  }
  .canvas {
    position: relative;
    width: 1200px;
    height: 1200px;
    background: var(--page);
  }
  .print {
    position: absolute;
    left: 151px;
    top: 25px;
    width: 883px;
    height: 1124px;
    background: var(--navy);
  }
  .frame {
    position: absolute;
    left: 224px;
    top: 75px;
    width: 747px;
    height: 1007px;
    box-sizing: border-box;
    border: 9px solid var(--olive);
  }
  .foliage {
    position: absolute;
    left: 594px;
    top: 463px;
    width: 368px;
    height: 610px;
  }
  .poem-column {
    position: absolute;
    top: 140px;
    text-align: center;
    font-family: "Questrial", sans-serif;
    font-size: 15px;
    line-height: 19.1px;
    color: var(--ink);
  }
  .poem-column--left { left: 252px; width: 380px; }
  .poem-column--right { left: 616px; width: 340px; }
  .stanza { margin: 0 0 19px; }
  .stanza--wide-gap { margin-bottom: 38px; }
  .drop-cap {
    position: absolute;
    left: 259px;
    top: 106px;
    font-family: "Great Vibes", cursive;
    font-size: 54px;
    line-height: 1;
    color: var(--gold);
  }
</style>
</head>
<body>
<div class="canvas">
  <div class="print"></div>
  <svg class="foliage" viewBox="0 0 368 610" role="img" aria-label="Jungle foliage with olive leaves, orange and yellow flowers, a butterfly and a dragonfly">
    <defs>
      <linearGradient id="foliage-tone" x1="0" y1="0" x2="1" y2="1">
        <stop offset="0" stop-color="#5b6429" stop-opacity="0"/>
        <stop offset="0.45" stop-color="#5b6429" stop-opacity="0.55"/>
        <stop offset="0.75" stop-color="#d88432" stop-opacity="0.6"/>
        <stop offset="1" stop-color="#f2bd3c" stop-opacity="0.7"/>
      </linearGradient>
    </defs>
    <rect width="368" height="610" fill="url(#foliage-tone)"/>
  </svg>
  <div class="frame"></div>

  <span class="drop-cap" aria-hidden="true">L</span>

  <div class="poem-column poem-column--left">
    <p class="stanza">&nbsp;&nbsp;&nbsp;&nbsp;ife’s journey began with a challenge<br>It was heralded far and near<br>The road led on foerever<br>it’s completion was known to be clear</p>
    <p class="stanza stanza--wide-gap">From the garden of light proceeded,<br>To the valley of shadows it led<br>Thorns and thistles adorned it<br>Past abyss and crevice it sped</p>
    <p class="stanza">The brave surged forward with courage<br>The wise undaunted pressed on<br>The mighty held their banner<br>We all awaited the dawn</p>
    <p class="stanza">Though the pitfalls and hazards were many<br>The pathways was clearly in view<br>Straight and sure it glided<br>It’s course we knew to be true</p>
    <p class="stanza">I knew you, Sweetheart beforehand<br>So precious and sweet were you<br>Our moments of bliss were priceless<br>Each day thought us joy anew</p>
    <p class="stanza">The call to progression beckoned,<br>At last I would have my chance-<br>to clasp you to me forever,<br>And seal our divine romance</p>
    <p class="stanza">I eagerly started the journey<br>Though with sorrow, I left you behind<br>With courage and faith I continued<br>Far I knew that you later I’d find</p>
    <p class="stanza">I dilignly searched for you, Darling<br>The roadway was both bleek and fair<br>Though the years grew long in number<br>I did not give up in despair</p>
  </div>

  <div class="poem-column poem-column--right">
    <p class="stanza">At last in distance I saw you,<br>So beautiful, lovely and sweet!<br>Your attention I struggled to capture,<br>Your love I wrested to meet</p>
    <p class="stanza">What rapture was mine in fulfillment<br>As now together we stand<br>To cherish and love each other,<br>While our plans and dreams expand</p>
    <p class="stanza">I love you, Darling, forever,<br>My life you have made replete,<br>Our eternal mansion beckons,<br>Your love has made it complete</p>
  </div>
</div>
</body>
</html>
```